Summer Drinks Flyer for Coffee Shop

We are a coffee shop in London and would like to have a cool and nice flyer for our summer drinks (juices and frozen drink) flyer - see on the attached file for the list

Attached you can find an "attempt" - please note that I would no necessary need the image below.

I also attache our new logo.

thank you

```html
<!DOCTYPE html>
<html lang="en">
<head>
<meta charset="utf-8">
<title>New Summer Drinks Menu</title>
<link rel="stylesheet" href="https://fonts.googleapis.com/css2?family=Great+Vibes&family=Oswald:wght@600;700&family=Comfortaa:wght@500&family=Open+Sans:ital,wght@1,700&display=swap">
<style>
  :root {
    --pink: #e8175d;
    --ink: #111111;
    --brown: #6b4a1f;
    --brown-tag: #7a2e16;
    --rule: #b9a98a;
    --paper: #ffffff;
    --gold: #f2c300;
  }
  * { box-sizing: border-box; margin: 0; padding: 0; }
  html, body { width: 937px; height: 1200px; overflow: hidden; background: var(--paper); }
  .flyer { position: relative; width: 937px; height: 1200px; background: var(--paper); overflow: hidden; }

  .splash {
    position: absolute; left: 0; top: 150px; width: 937px; height: 640px;
    background:
      radial-gradient(ellipse 120px 260px at 40px 260px, rgba(240,200,0,.75), transparent 70%),
      radial-gradient(ellipse 160px 120px at 130px 120px, rgba(230,40,110,.55), transparent 70%),
      radial-gradient(ellipse 140px 90px at 260px 70px, rgba(245,140,20,.55), transparent 70%),
      radial-gradient(ellipse 110px 80px at 380px 30px, rgba(130,60,170,.45), transparent 70%),
      radial-gradient(ellipse 90px 220px at 920px 300px, rgba(120,190,40,.55), transparent 70%),
      radial-gradient(ellipse 120px 200px at 60px 440px, rgba(230,40,110,.35), transparent 70%);
  }
  .panel {
    position: absolute; left: 55px; top: 245px; width: 860px; height: 800px;
    background: linear-gradient(180deg, rgba(255,255,255,.92), rgba(250,244,232,.92));
  }

  .title { position: absolute; left: 0; top: 0; width: 937px; height: 240px; }
  .script { font-family: "Great Vibes", cursive; fill: var(--ink); }
  .headline { font-family: "Oswald", sans-serif; font-weight: 700; fill: var(--pink); }

  .section-title {
    position: absolute; left: 81px;
    font-family: "Comfortaa", sans-serif; font-weight: 500; font-size: 52px;
    color: var(--pink); line-height: 1; padding-bottom: 8px;
    border-bottom: 1.5px solid var(--rule); letter-spacing: 1px; white-space: nowrap;
  }
  .items {
    position: absolute; left: 82px; list-style: none;
    font-family: "Open Sans", sans-serif; font-style: italic; font-weight: 700;
    font-size: 25px; line-height: 34px; color: var(--ink); letter-spacing: 1px;
  }
  .items li::before { content: "\2022"; margin-right: 8px; }

  .drink-photo { position: absolute; border-radius: 10px; }
  .drink-frozen { left: 633px; top: 242px; width: 99px; height: 174px;
    background: linear-gradient(180deg, #f7c4cc, #ef8f9d 60%, #f4d6da); }
  .drink-juice { left: 575px; top: 440px; width: 190px; height: 236px;
    background: linear-gradient(180deg, #f6c37a, #ef9a28 55%, #f2a23b); }
  .drink-coffee { left: 610px; top: 732px; width: 144px; height: 205px;
    background: linear-gradient(180deg, #efe2d2, #c9a98a 60%, #a8876a); }

  .price { position: absolute; width: 124px; height: 124px; }
  .price-text { font-family: "Open Sans", sans-serif; font-style: normal; font-weight: 700; font-size: 25px; fill: #fff; }

  .tag { position: absolute; }
  .tag-text { font-family: "Oswald", sans-serif; fill: #fff; }
  .tag-note { fill: var(--gold); font-weight: 600; }

  .footer-curve { position: absolute; left: 0; top: 900px; width: 937px; height: 300px; }
  .fruit-photo { position: absolute; left: 22px; top: 1018px; width: 470px; height: 165px; border-radius: 40px;
    background: linear-gradient(90deg, #f3d23a, #d82a2a 35%, #f0a23a 65%, #8fb83a); }

  .brand { position: absolute; left: 590px; top: 1080px; width: 300px; text-align: center; color: var(--ink); }
  .brand-line { display: flex; align-items: center; justify-content: center; gap: 12px; }
  .brand-dot { width: 28px; height: 28px; border-radius: 50%; background: var(--brown); }
  .brand-name { font-family: "Comfortaa", sans-serif; font-weight: 500; font-size: 48px; line-height: 1; }
  .brand-tagline { font-family: "Comfortaa", sans-serif; font-weight: 500; font-size: 14px; letter-spacing: 1px; margin-top: 10px; color: var(--ink); }
</style>
</head>
<body>
<main class="flyer">
  <div class="splash" role="img" aria-label="Colourful paint splash decoration"></div>
  <div class="panel"></div>

  <svg class="title" viewBox="0 0 937 240">
    <text class="script" x="112" y="88" font-size="68">New</text>
    <text class="headline" x="55" y="184" font-size="128" textLength="822" lengthAdjust="spacingAndGlyphs">Summer Drinks</text>
    <text class="script" x="672" y="220" font-size="68">Menu</text>
  </svg>

  <h2 class="section-title" style="top:280px; width:543px">Frozen Fruit Drinks</h2>
  <ul class="items" style="top:354px">
    <li>Strawberry &amp; banana, Pineapple</li>
    <li>mango and banana</li>
  </ul>

  <h2 class="section-title" style="top:442px; width:340px">Fruit Juices</h2>
  <ul class="items" style="top:507px">
    <li>Orange and carrot</li>
    <li>Orange and pineapple</li>
    <li>Pineapple and apple</li>
    <li>Apple and kiwi</li>
    <li>Carrot and ginger</li>
  </ul>

  <h2 class="section-title" style="top:700px; width:380px">Iced-Coffees</h2>
  <ul class="items" style="top:766px">
    <li>Orange and carrot</li>
    <li>Orange and pineapple</li>
    <li>Pineapple and apple</li>
    <li>Apple and kiwi</li>
    <li>Carrot and ginger</li>
  </ul>

  <div class="drink-photo drink-frozen" role="img" aria-label="Strawberry smoothie in a glass"></div>
  <div class="drink-photo drink-juice" role="img" aria-label="Orange and carrot juice with fruit"></div>
  <div class="drink-photo drink-coffee" role="img" aria-label="Iced coffee in a glass"></div>

  <svg class="price" style="left:767px; top:264px" viewBox="0 0 124 124">
    <polygon fill="var(--pink)" points="62,0 69,15 82,3 84,19 100,11 97,27 115,25 106,40 123,44 110,55 124,62 110,69 123,80 106,84 115,99 97,97 100,113 84,105 82,121 69,109 62,124 55,109 42,121 40,105 24,113 27,97 9,99 18,84 1,80 14,69 0,62 14,55 1,44 18,40 9,25 27,27 24,11 40,19 42,3 55,15"/>
    <circle cx="62" cy="62" r="44" fill="none" stroke="#fff" stroke-width="2"/>
    <text class="price-text" x="62" y="71" text-anchor="middle">€2.95</text>
  </svg>
  <svg class="price" style="left:767px; top:503px" viewBox="0 0 124 124">
    <polygon fill="var(--pink)" points="62,0 69,15 82,3 84,19 100,11 97,27 115,25 106,40 123,44 110,55 124,62 110,69 123,80 106,84 115,99 97,97 100,113 84,105 82,121 69,109 62,124 55,109 42,121 40,105 24,113 27,97 9,99 18,84 1,80 14,69 0,62 14,55 1,44 18,40 9,25 27,27 24,11 40,19 42,3 55,15"/>
    <circle cx="62" cy="62" r="44" fill="none" stroke="#fff" stroke-width="2"/>
    <text class="price-text" x="62" y="71" text-anchor="middle">€2.95</text>
  </svg>
  <svg class="price" style="left:767px; top:772px" viewBox="0 0 124 124">
    <polygon fill="var(--pink)" points="62,0 69,15 82,3 84,19 100,11 97,27 115,25 106,40 123,44 110,55 124,62 110,69 123,80 106,84 115,99 97,97 100,113 84,105 82,121 69,109 62,124 55,109 42,121 40,105 24,113 27,97 9,99 18,84 1,80 14,69 0,62 14,55 1,44 18,40 9,25 27,27 24,11 40,19 42,3 55,15"/>
    <circle cx="62" cy="62" r="44" fill="none" stroke="#fff" stroke-width="2"/>
    <text class="price-text" x="62" y="71" text-anchor="middle">€2.45</text>
  </svg>

  <svg class="tag" style="left:380px; top:462px" width="200" height="200" viewBox="0 0 200 200">
    <path d="M45 12 Q75 10 92 55" fill="none" stroke="#444" stroke-width="1.5"/>
    <g transform="rotate(-12 120 120)">
      <path d="M70 45 L135 45 Q145 45 145 55 L145 185 Q145 195 135 195 L70 195 Q60 195 60 185 L60 55 Q60 45 70 45 Z" fill="var(--pink)"/>
      <circle cx="102" cy="60" r="6" fill="#fff"/>
      <text class="tag-text" x="102" y="118" text-anchor="middle" font-size="40" font-weight="700">Free</text>
      <text class="tag-text tag-note" x="102" y="150" text-anchor="middle" font-size="22">Mint or</text>
      <text class="tag-text tag-note" x="102" y="175" text-anchor="middle" font-size="22">Ginger</text>
    </g>
  </svg>

  <svg class="tag" style="left:430px; top:730px" width="200" height="200" viewBox="0 0 200 200">
    <path d="M30 15 Q65 8 82 55" fill="none" stroke="#444" stroke-width="1.5"/>
    <g transform="rotate(-8 110 120)">
      <path d="M60 45 L135 45 Q145 45 145 55 L145 180 Q145 190 135 190 L60 190 Q50 190 50 180 L50 55 Q50 45 60 45 Z" fill="var(--brown-tag)"/>
      <circle cx="97" cy="60" r="6" fill="#fff"/>
      <text class="tag-text" x="97" y="105" text-anchor="middle" font-size="30" font-weight="700">Syrup</text>
      <text class="tag-text" x="97" y="138" text-anchor="middle" font-size="30" font-weight="700">shot</text>
      <text class="tag-text tag-note" x="97" y="170" text-anchor="middle" font-size="21">@10p</text>
    </g>
  </svg>

  <svg class="footer-curve" viewBox="0 0 937 300" preserveAspectRatio="none">
    <path d="M0 34 Q420 140 937 118 L937 300 L0 300 Z" fill="var(--paper)"/>
    <path d="M0 34 Q420 140 937 118" fill="none" stroke="var(--brown)" stroke-width="6"/>
    <path d="M0 26 Q300 102 700 113" fill="none" stroke="var(--brown)" stroke-width="2"/>
  </svg>

  <div class="fruit-photo" role="img" aria-label="Bananas, strawberries, mango and pineapple"></div>

  <div class="brand">
    <div class="brand-line">
      <span class="brand-dot"></span>
      <span class="brand-name">Solaro</span>
    </div>
    <div class="brand-tagline">CAFÉ AND PASTRY HOUSE</div>
  </div>
</main>
</body>
</html>
```